2 sided flyer for Insurance Servics

Would like a flyer that talks about who we are, our services, and our process. Attaching relevant information, as well as our Logo and other logos for a few larger insurance carriers that we have access to.

Target Market(s)

Financial Advisors and Insurance Agents

Industry/Entity Type

Finance and Insurance

Colors
0054AA
0677BA
7BADD7
CADEEF
E8F1F8
F0912C
F2A743
F7CA91
FBE8D2
FDF5EE

Requirements
Must have
• Lists, bullet points, pictures, and logos uploaded

```html
<!DOCTYPE html>
<html lang="en">
<head>
<meta charset="utf-8">
<title>Summit Coverage Group – Two-Sided Flyer</title>
<link rel="stylesheet" href="https://fonts.googleapis.com/css2?family=Barlow+Condensed:wght@400;500;600;700&family=Barlow+Semi+Condensed:ital,wght@0,400;0,500;0,600;0,700;1,500;1,600&display=swap">
<style>
:root{
  --navy:#251d63;
  --gold:#e9c54c;
  --ink:#1f1f3a;
  --grey:#e3e3ea;
  --stage:#a3a3a3;
  --white:#ffffff;
}
*{margin:0;padding:0;box-sizing:border-box}
html,body{width:1200px;height:2387px;overflow:hidden}
body{background:var(--stage);font-family:"Barlow Semi Condensed",sans-serif;color:var(--ink);position:relative;font-size:13px}
.page{position:absolute;left:200px;width:821px;height:1064px;background:var(--white);overflow:hidden;box-shadow:0 2px 10px rgba(0,0,0,.25)}
.page--front{top:100px}
.page--back{top:1218px}
.abs{position:absolute}
p{font-size:13px;line-height:17px}

/* header */
.brand{left:26px;top:24px;display:flex;align-items:center;gap:12px}
.brand__mark{width:78px;height:78px;background:#cfd0d8}
.brand__name{font-family:"Barlow Condensed",sans-serif;font-weight:700;font-size:27px;line-height:26px;color:var(--navy);letter-spacing:.3px}
.header-bar{left:346px;top:20px;width:475px;height:100px;background:var(--navy);color:var(--white);text-align:center;padding-top:10px}
.header-bar__kicker{font-family:"Barlow Condensed",sans-serif;font-size:24px;font-weight:500;display:flex;align-items:center;justify-content:center;gap:10px}
.header-bar__kicker::before,.header-bar__kicker::after{content:"";width:38px;height:2px;background:var(--gold)}
.header-bar__title{font-family:"Barlow Condensed",sans-serif;font-size:58px;font-weight:500;line-height:54px;letter-spacing:-.5px}
.header-wedge{left:322px;top:0;width:30px;height:138px;background:#d9d9df;clip-path:polygon(0 0,100% 20%,100% 100%,0 100%)}

.intro{left:0;top:138px;width:821px;height:116px;background:var(--gold);padding:12px 27px}
.intro p{font-size:14px;line-height:17.8px}

.photo{background:linear-gradient(160deg,#c7d2df 0%,#8a9bb3 45%,#3f4e6b 100%)}
.front-photo{left:0;top:269px;width:329px;height:297px}
.services-tab{left:0;top:566px;width:329px;height:33px;background:var(--gold);clip-path:polygon(0 0,100% 0,92% 100%,0 100%);padding:2px 20px;font-family:"Barlow Condensed",sans-serif;font-size:24px;color:var(--navy)}
.services-tab b{font-weight:700}
.services-box{left:13px;top:599px;width:287px;height:250px;background:linear-gradient(180deg,#e4e4ec 0%,#ece6cf 70%,#f2d98e 100%);padding:10px 12px 0 14px}
.services-box p{text-align:justify;color:var(--navy);font-size:14.3px;line-height:17.8px}
.services-quote{margin-top:14px;text-align:center;color:var(--navy);font-size:13.5px;line-height:17px}
.services-quote em{display:block;font-weight:600}

.benefits__lead{left:343px;top:272px;width:470px;font-size:14px}
.benefit{left:343px;width:470px;display:flex;gap:20px}
.benefit--1{top:306px}.benefit--2{top:409px}.benefit--3{top:529px}.benefit--4{top:649px}
.benefit__icon{flex:0 0 60px;height:60px;background:var(--navy);margin-top:8px;display:flex;align-items:center;justify-content:center}
.benefit h3{font-family:"Barlow Condensed",sans-serif;font-size:15px;line-height:17px;font-weight:700;color:var(--navy)}
.benefit p{text-align:justify;font-size:14px;line-height:17px}
.closing-text{left:347px;top:758px;width:466px}
.closing-text p{font-size:13.5px;line-height:17px}
.cta{display:flex;margin:1px 0}
.cta__label{background:var(--navy);color:#fff;font-weight:700;font-size:12px;padding:1px 18px;border-radius:10px 0 0 10px}
.cta__mail{background:var(--gold);color:var(--navy);font-weight:700;font-size:12px;padding:1px 22px;border-radius:0 10px 10px 0}

.strategists{left:0;top:857px;width:821px;height:168px;background:var(--navy);color:#fff}
.strategists__box{left:16px;top:13px;width:144px;height:141px;background:var(--gold);text-align:center;padding-top:34px;font-family:"Barlow Condensed",sans-serif;font-weight:700;font-size:20px;line-height:23px;color:var(--navy)}
.strategists__box::after{content:"";display:block;width:90px;height:3px;background:var(--navy);margin:7px auto 0}
.strategists__list{left:185px;top:11px;width:621px}
.strategists__list p,.strategists__list li{font-size:14px;line-height:17.8px}
.strategists__list li{list-style:none;position:relative;padding-left:17px}
.strategists__list li::before{content:"";position:absolute;left:2px;top:4px;border-left:8px solid #fff;border-top:5px solid transparent;border-bottom:5px solid transparent}
.strategists__list b{color:var(--gold);font-weight:700}

.footer{left:0;top:1025px;width:821px;height:39px;display:flex;align-items:center;padding-left:15px;gap:14px;font-size:13px}
.footer__item{display:flex;align-items:center;gap:7px}
.footer__icon{width:21px;height:21px;border-radius:50%;background:var(--gold);display:flex;align-items:center;justify-content:center}
.footer__web{font-weight:700;color:var(--navy)}

/* back */
.back-photo{left:0;top:0;width:353px;height:254px;background:linear-gradient(135deg,#eef0f2 0%,#b9c2c9 40%,#7b6f66 75%,#3e3d44 100%)}
.concierge{left:353px;top:0;width:468px;height:254px;background:var(--gold)}
.concierge__title{left:26px;top:25px;width:415px;height:37px;background:var(--navy);color:#fff;text-align:center;font-family:"Barlow Condensed",sans-serif;font-weight:600;font-size:23px;line-height:37px}
.concierge__text{left:26px;top:72px;width:416px;text-align:justify;color:var(--navy)}
.concierge__text p{font-size:14.5px;line-height:18px;font-weight:500}
.concierge__quote{left:24px;top:162px;width:417px;height:74px;background:#fff;text-align:center;color:var(--navy);padding-top:6px;font-size:14.5px}
.concierge__quote em{display:block;font-weight:600;font-size:17.5px;line-height:22px}

.features{top:264px}
.features--left{left:10px;width:390px}
.features--right{left:410px;width:400px}
.feature{position:relative;padding-left:25px;margin-bottom:1px}
.feature svg{position:absolute;left:0;top:0}
.feature h4{font-family:"Barlow Condensed",sans-serif;font-weight:700;font-size:14px;line-height:16px;color:var(--navy)}
.feature p{font-size:13.4px;line-height:16.6px}
.side-quote{left:434px;top:576px;width:366px;height:68px;background:var(--grey);text-align:center;color:var(--navy);padding-top:9px;font-size:13px;line-height:17px}
.side-quote em{display:block;font-weight:600}

.wide-quote{left:0;top:655px;width:821px;height:59px;background:var(--gold);text-align:center;padding-top:10px;color:var(--navy);font-size:13px;line-height:18px}
.wide-quote em{font-weight:600}

.process{left:0;top:714px;width:821px;height:310px;background:var(--navy);color:#fff}
.process__list{left:22px;top:11px;width:530px}
.process__list h5{font-family:"Barlow Condensed",sans-serif;font-weight:700;font-size:14px;line-height:17px}
.process__list h6{font-family:"Barlow Condensed",sans-serif;font-weight:700;font-size:14px;line-height:17px;color:var(--gold)}
.process__list p{font-size:13px;line-height:17px}
.carriers{left:559px;top:16px;width:238px;height:278px;background:#fff;text-align:center;color:var(--navy)}
.carriers__title{display:inline-block;margin-top:9px;background:var(--grey);padding:2px 14px;font-family:"Barlow Condensed",sans-serif;font-weight:700;font-size:14.5px}
.carriers__list{font-family:"Barlow Condensed",sans-serif;font-size:14px;line-height:17px;margin:12px 10px 0;font-weight:500}
.carriers__badges{display:flex;flex-wrap:wrap;justify-content:center;gap:10px 14px;margin-top:14px}
.badge{background:#d2d6e6}
</style>
</head>
<body>

<section class="page page--front">
  <div class="abs header-wedge"></div>
  <div class="abs brand">
    <div class="brand__mark"></div>
    <div class="brand__name">SUMMIT<br>COVERAGE<br>GROUP LLC</div>
  </div>
  <div class="abs header-bar">
    <div class="header-bar__kicker">ONE-STOP SHOP FOR ALL LIFE</div>
    <div class="header-bar__title">INSURANCE SOLUTIONS</div>
  </div>

  <div class="abs intro">
    <p><b>SUMMIT COVERAGE GROUP is a full-service life insurance Brokerage General Agency (BGA) and serves financial advisors, independent insurance agents, and banks throughout the United States.</b> Having served our customers for over 25 years, we are committed to helping financial advisors achieve their goals for their clients. Serving as a one-stop shop for all life insurance solutions, we offer a wide range of insurance products from multiple carriers, giving our advisors and agents access to a variety of options and solutions to meet their clients' needs.</p>
  </div>

  <div class="abs photo front-photo" role="img" aria-label="Photo of a businessman holding an umbrella over a city skyline"></div>
  <div class="abs services-tab">OUR <b>SERVICES</b></div>
  <div class="abs services-box">
    <p>As a BGA, our mission is to connect agents and advisors with insurance carriers and help our customers find the correct product that meets each client's needs. From our experienced Point of Sale Strategists to our professional Concierge Service Team, we provide value every step of the way, at no additional cost!</p>
    <div class="services-quote"><em>“From quote to issue and review to service, each case is an opportunity of quality care.”</em>- Dana P, New Business Specialist</div>
  </div>

  <p class="abs benefits__lead">When you chose to work with SCG, you will add value to your firm..overnight!</p>
  <div class="abs benefit benefit--1">
    <div class="benefit__icon"><svg width="38" height="34" viewBox="0 0 38 34"><path d="M19 6 L33 30 H5 Z" fill="#e9c54c"/><rect x="17.5" y="13" width="3" height="9" fill="#251d63"/><rect x="17.5" y="24" width="3" height="3" fill="#251d63"/></svg></div>
    <div><h3>IMMEDIATE RISK MANAGEMENT PARTNER</h3><p>We know insurance and understand your business. Your agents will have access to a wide range of carriers, giving them options to meet client needs. In addition, we only deal in insurance...so rest assured we leave the money management to you!</p></div>
  </div>
  <div class="abs benefit benefit--2">
    <div class="benefit__icon"><svg width="34" height="38" viewBox="0 0 34 38"><path d="M17 2 L31 8 V19 C31 28 24 34 17 36 C10 34 3 28 3 19 V8 Z" fill="#e9c54c"/><path d="M10 19 L15 24 L25 13" stroke="#251d63" stroke-width="3.5" fill="none"/></svg></div>
    <div><h3>EXPERIENCED INSURANCE SPECIALISTS</h3><p>Our Point of Sales Specialists have many years of industry experience, hold various designations, and are licensed to provide a variety of products. These trained professionals are located throughout the country and are ready to provide prompt service to your staff.</p></div>
  </div>
  <div class="abs benefit benefit--3">
    <div class="benefit__icon"><svg width="38" height="34" viewBox="0 0 38 34"><circle cx="24" cy="9" r="6" fill="#e9c54c"/><path d="M3 20 H12 L20 24 H30 L35 21 V26 L24 32 H3 Z" fill="#fff"/></svg></div>
    <div><h3>CUSTOMIZED CONCIERGE SERVICE</h3><p>This team of professionals leverage their experience &amp; technology to remove the pain points of writing policies. Comprised of our licensing, application, and case management specialists, we handle every aspect of the process. No more application paperwork or underwriting hassle for your staff!</p></div>
  </div>
  <div class="abs benefit benefit--4">
    <div class="benefit__icon"><svg width="38" height="34" viewBox="0 0 38 34"><circle cx="24" cy="10" r="8" fill="#e9c54c"/><path d="M3 20 H12 L20 24 H30 L35 21 V26 L24 32 H3 Z" fill="#fff"/></svg></div>
    <div><h3>SAVE TIME AND MONEY</h3><p>We have designed our services to operate efficiently, funded from the compensation we receive by the insurance carriers, meaning no cost to you. Our goal is to increase your production, while eliminating your internal salaries and benefits dedicated to insurance support.</p></div>
  </div>

  <div class="abs closing-text">
    <p>At SCG, we are dedicated to developing lasting relationships with all our of our customers, both current &amp; new. If you have any insurance questions or would like to know how best to work with SCG,</p>
    <div class="cta"><span class="cta__label">Please contact us today contact</span><span class="cta__mail">info@summit-coverage.com</span></div>
    <p>We look forward to using our expertise to help you grow your business.</p>
  </div>

  <div class="abs strategists">
    <div class="abs strategists__box">OUR POINT<br>OF SALE<br>STRATEGISTS</div>
    <div class="abs strategists__list">
      <p>work directly with agents and advisors to provide experienced assistance for immediate client needs, as well as maximizing insurance planning to find opportunities for all clients.</p>
      <ul>
        <li><b>DEDICATED STRATEGISTS</b> – We develop a personal relationship with each advisor, giving you confidence that we are working in your best interest. Always here to help with quotes and analysis.</li>
        <li><b>QUOTES MADE EASY</b> - Access our online system or simply email your specialist to receive quotes for your client reviews, life event circumstances, estate needs, or prospect meetings.</li>
        <li><b>NATIONAL FOOTPRINT</b> – Our team is nationwide, allowing us to serve you regardless of location, time zone, or licensing limitations.</li>
      </ul>
    </div>
  </div>

  <div class="abs footer">
    <span class="footer__item"><span class="footer__icon"><svg width="11" height="14" viewBox="0 0 11 14"><path d="M5.5 0 C2.5 0 0 2.3 0 5.2 C0 9 5.5 14 5.5 14 S11 9 11 5.2 C11 2.3 8.5 0 5.5 0 Z" fill="#251d63"/><circle cx="5.5" cy="5.2" r="2" fill="#e9c54c"/></svg></span>1200 Lakeview Drive, Suite 210, Springfield, IL 62704</span>
    <span class="footer__item"><span class="footer__icon"><svg width="12" height="12" viewBox="0 0 12 12"><path d="M2 0 L4.5 3 L3.2 4.6 C4 6.3 5.7 8 7.4 8.8 L9 7.5 L12 10 L10 12 C5 11.5 0.5 7 0 2 Z" fill="#251d63"/></svg></span>555-010-4821 / 1-800-555-0199</span>
    <span class="footer__item footer__web"><span class="footer__icon"><svg width="13" height="13" viewBox="0 0 13 13"><circle cx="6.5" cy="6.5" r="5.5" fill="none" stroke="#251d63" stroke-width="1.5"/><path d="M1 6.5 H12 M6.5 1 C3.5 4 3.5 9 6.5 12 C9.5 9 9.5 4 6.5 1" fill="none" stroke="#251d63" stroke-width="1.2"/></svg></span>summitcoveragegroup.com</span>
  </div>
</section>

<section class="page page--back">
  <div class="abs back-photo" role="img" aria-label="Photo of a team of colleagues gathered around a laptop in a bright office"></div>
  <div class="abs concierge">
    <div class="abs concierge__title">OUR CONCIERGE SERVICE TEAM</div>
    <div class="abs concierge__text"><p>Our Concierge Service Team is comprised of several specialists. Once an agent moves forward with an application, simply hand it off to our staff, ensuring your policy is processed accurately and delivered in a timely manner.</p></div>
    <div class="abs concierge__quote"><em>“We are the go-to-person for anything the agent needs; we handle everything from A to Z!”</em>– Rachel T, Application Specialist/Case Manager</div>
  </div>

  <div class="abs features features--left">
    <div class="feature"><svg width="19" height="19" viewBox="0 0 19 19"><circle cx="9.5" cy="9.5" r="8" fill="none" stroke="#e9c54c" stroke-width="2"/><path d="M5 9.5 L8.5 13 L16 3" stroke="#e9c54c" stroke-width="2.4" fill="none"/></svg><h4>DEDICATED CASE MANAGERS</h4><p>Your personal case manager gives us a better understanding of your business, expectations, and preferred process.</p></div>
    <div class="feature"><svg width="19" height="19" viewBox="0 0 19 19"><circle cx="9.5" cy="9.5" r="8" fill="none" stroke="#e9c54c" stroke-width="2"/><path d="M5 9.5 L8.5 13 L16 3" stroke="#e9c54c" stroke-width="2.4" fill="none"/></svg><h4>CARRIER FAMILIARITY</h4><p>Our experience enables us to provide correct forms from the get-go, as well as properly relay carrier specific processes and manage expectations.</p></div>
    <div class="feature"><svg width="19" height="19" viewBox="0 0 19 19"><circle cx="9.5" cy="9.5" r="8" fill="none" stroke="#e9c54c" stroke-width="2"/><path d="M5 9.5 L8.5 13 L16 3" stroke="#e9c54c" stroke-width="2.4" fill="none"/></svg><h4>AGENT LICENSING</h4><p>We confirm you are correcly licensed and appointed before applications are initiated. If appointment is needed, we help you get this done in a timely, technology efficient manner.</p></div>
    <div class="feature"><svg width="19" height="19" viewBox="0 0 19 19"><circle cx="9.5" cy="9.5" r="8" fill="none" stroke="#e9c54c" stroke-width="2"/><path d="M5 9.5 L8.5 13 L16 3" stroke="#e9c54c" stroke-width="2.4" fill="none"/></svg><h4>NO HASSLE PAPERWORK</h4><p>Our team will handle all application &amp; underwriting needs, assuring a efficient process and less hassle for the agent.</p></div>
    <div class="feature"><svg width="19" height="19" viewBox="0 0 19 19"><circle cx="9.5" cy="9.5" r="8" fill="none" stroke="#e9c54c" stroke-width="2"/><path d="M5 9.5 L8.5 13 L16 3" stroke="#e9c54c" stroke-width="2.4" fill="none"/></svg><h4>NO FLUFF PROCESS</h4><p>We create a seamless process by gathering what is required for underwriting, eliminating the unnecessary back and forth with clients that often delays the policy and annoys clients.</p></div>
    <div class="feature"><svg width="19" height="19" viewBox="0 0 19 19"><circle cx="9.5" cy="9.5" r="8" fill="none" stroke="#e9c54c" stroke-width="2"/><path d="M5 9.5 L8.5 13 L16 3" stroke="#e9c54c" stroke-width="2.4" fill="none"/></svg><h4>CLIENT CONFIDENTIALITY</h4><p>Our application specialist contacts the client and takes the application, eliminating the need for clients to share personal medical information with their advisor.</p></div>
  </div>

  <div class="abs features features--right">
    <div class="feature"><svg width="19" height="19" viewBox="0 0 19 19"><circle cx="9.5" cy="9.5" r="8" fill="none" stroke="#e9c54c" stroke-width="2"/><path d="M5 9.5 L8.5 13 L16 3" stroke="#e9c54c" stroke-width="2.4" fill="none"/></svg><h4>PROACTIVE APPROACH</h4><p>We proactively order medical records and exams for most cases, speeding up the UW process by days if not weeks, resulting in quicker decisions.</p></div>
    <div class="feature"><svg width="19" height="19" viewBox="0 0 19 19"><circle cx="9.5" cy="9.5" r="8" fill="none" stroke="#e9c54c" stroke-width="2"/><path d="M5 9.5 L8.5 13 L16 3" stroke="#e9c54c" stroke-width="2.4" fill="none"/></svg><h4>ELECTRONIC SIGNATURES</h4><p>By leveraging technology, we will utilize electronic signature capabilities for both agent and client, speeding up the overall process.</p></div>
    <div class="feature"><svg width="19" height="19" viewBox="0 0 19 19"><circle cx="9.5" cy="9.5" r="8" fill="none" stroke="#e9c54c" stroke-width="2"/><path d="M5 9.5 L8.5 13 L16 3" stroke="#e9c54c" stroke-width="2.4" fill="none"/></svg><h4>RECURRING UPDATES</h4><p>Your case manager will keep you updated on the status of all cases.</p></div>
    <div class="feature"><svg width="19" height="19" viewBox="0 0 19 19"><circle cx="9.5" cy="9.5" r="8" fill="none" stroke="#e9c54c" stroke-width="2"/><path d="M5 9.5 L8.5 13 L16 3" stroke="#e9c54c" stroke-width="2.4" fill="none"/></svg><h4>ONLINE CASE TRACKER</h4><p>This tool allows you to access the status of your cases.<br>All carriers. All cases. All the time.</p></div>
    <div class="feature"><svg width="19" height="19" viewBox="0 0 19 19"><circle cx="9.5" cy="9.5" r="8" fill="none" stroke="#e9c54c" stroke-width="2"/><path d="M5 9.5 L8.5 13 L16 3" stroke="#e9c54c" stroke-width="2.4" fill="none"/></svg><h4>POLICY DELIVERY</h4><p>we ensure premiums are paid and policy documents<br>are delivered.</p></div>
  </div>
  <div class="abs side-quote"><em>“Our weekly updates keep advisors well informed<br>throughout the process.”</em>– Jordan M, Senior Case Manager</div>

  <div class="abs wide-quote"><em>“Oftentimes clients can be uncomfortable disclosing personal health history to their advisor, but will answer<br>freely with someone in my role. I let clients know we have their best interest at heart.”</em> – Marisol K, Application Specialist</div>

  <div class="abs process">
    <div class="abs process__list">
      <h5>OUR PROCESS</h5>
      <h6>1. QUOTES &amp; ANALYSIS</h6>
      <p>a. Access to multiple carriers, including most industry leaders.<br>b. Submit quotes online or simply email our staff.<br>c. Consult our Specialists to find the best solution for your client.</p>
      <h6>2. LICENSING &amp; APPOINTMENT</h6>
      <p>a. Confirm agent license and appointment is up to date.<br>b. If necessary, use our assistance to get appointed in a timely manner.<br>c. Electronic signatures make the appointment process fast and easy.</p>
      <h6>3. APPLICATIONS &amp; UNDERWRITING</h6>
      <p>a. Our specialists oversee the entire application and underwriting process.<br>b. Direct contact with the client, ensuring confidential &amp; private medical history conversation.<br>c. Utilize technology to provide electronic signatures where possible.</p>
      <h6>4. POLICY DELIVERY &amp; PAYOUT</h6>
      <p>a. Ensure policy documents are delivered in full and on time.<br>b. Confirm premiums are paid and policies are in force.<br>c. Facilitate payout for all of your policies.</p>
    </div>
    <div class="abs carriers">
      <div class="carriers__title">LIST OF CARRIERS INCLUDE:</div>
      <div class="carriers__list">VALCREST LIFE • ORVANE • THISTLEMOOR LIFE • KELBROOK • MARROWIND MUTUAL • MUTUAL OF TALLGRASS • QUENTON NATIONAL • LARKHAVEN LIFE • PELWICK LIFE • DUNMORE RIDGE • FENWARDE • BRISENHOLT</div>
      <div class="carriers__badges">
        <span class="badge" style="width:56px;height:26px"></span>
        <span class="badge" style="width:80px;height:26px"></span>
        <span class="badge" style="width:120px;height:30px;border-radius:15px"></span>
        <span class="badge" style="width:56px;height:20px"></span>
        <span class="badge" style="width:64px;height:20px"></span>
        <span class="badge" style="width:64px;height:20px"></span>
      </div>
    </div>
  </div>

  <div class="abs footer">
    <span class="footer__item"><span class="footer__icon"><svg width="11" height="14" viewBox="0 0 11 14"><path d="M5.5 0 C2.5 0 0 2.3 0 5.2 C0 9 5.5 14 5.5 14 S11 9 11 5.2 C11 2.3 8.5 0 5.5 0 Z" fill="#251d63"/><circle cx="5.5" cy="5.2" r="2" fill="#e9c54c"/></svg></span>1200 Lakeview Drive, Suite 210, Springfield, IL 62704</span>
    <span class="footer__item"><span class="footer__icon"><svg width="12" height="12" viewBox="0 0 12 12"><path d="M2 0 L4.5 3 L3.2 4.6 C4 6.3 5.7 8 7.4 8.8 L9 7.5 L12 10 L10 12 C5 11.5 0.5 7 0 2 Z" fill="#251d63"/></svg></span>555-010-4821 / 1-800-555-0199</span>
    <span class="footer__item footer__web"><span class="footer__icon"><svg width="13" height="13" viewBox="0 0 13 13"><circle cx="6.5" cy="6.5" r="5.5" fill="none" stroke="#251d63" stroke-width="1.5"/><path d="M1 6.5 H12 M6.5 1 C3.5 4 3.5 9 6.5 12 C9.5 9 9.5 4 6.5 1" fill="none" stroke="#251d63" stroke-width="1.2"/></svg></span>summitcoveragegroup.com</span>
  </div>
</section>

</body>
</html>
```